Electrictrian Contractor Website Design

We are working with an electrical contractor in California called Quill Electric.

Some sites to use for content/competitors and inspiration:
https://corvinelectric.net
https://tulipmarsh.site/web/contractor/ (lots of contractor website designs we've approved and continue to show clients)

Thank you for taking the time to consider designing a website for us. We are web developers based in Stockton, CA, USA. Most of our projects go through the same process. Understanding this process may help you win a project with us. We custom-code all of our websites in-house. We don’t have any requirements as to what tools you use for your design, but we prefer Figma files. For any design that we label as four-stars, we send it to the client for review. The client picks the final design they want us to use. Once we complete this process, we will continue to show additional clients all the four-star sites and purchase them later. Your designs will have multiple chances to sell. For better chances of success, we ask that you follow these guidelines.

IMAGES:
If you use any images or icons in the design, we ask that you have a link to the asset so we can purchase the image/icon. Most of the designs we submit do not have the customer’s images on them unless they have some great images. Be creative; show us the feeling you are trying to portray with your image choices. Use any royalty-free site you choose. We subscribe to Quenvo and mainly use their images, but we can purchase images outside of Quenvo.

PLEASE NOTE: we will not submit designs to clients with watermarks on the images.

FONTS:
We ask that you identify the fonts used in the design. This can be done in a message if you want. We typically use Zentrik Fonts and Quenvo Fonts.

CONTENT:
We're always open to different content and ideas. We often submit designs with stock images so the client can see our vision. We typically take pictures after the website launch to use their images with our vision. Lorem Ipsum is fine for paragraphs, but we ask that you write the headers in correct English. We want to be able to show the vision and identify the sections of the website.

INSPIRATION:
We typically add a couple of links in the brief of websites we like to help you get started in your design.

REVISIONS:
We do not often ask for revisions of the designs unless we see something in the design that may not appeal to the client. If there are slight changes that we want to make, we do that in the development process.

FEEDBACK:
We rarely give feedback on designs during the design process. We are working on many website projects and do not have the time to provide feedback. We usually respond if your request is well thought out and asks specific questions, but a note asking “feedback, please” usually goes unanswered

```html
<!DOCTYPE html>
<html lang="en">
<head>
<meta charset="utf-8">
<title>Quill Electric</title>
<link href="https://fonts.googleapis.com/css2?family=Inter:wght@300;400;500;600;700;800&display=swap" rel="stylesheet">
<style>
:root{
  --blue:#0d3f8e;
  --blue-deep:#0a3273;
  --yellow:#f5b400;
  --ink:#1e2a3a;
  --muted:#5d6673;
  --line:#c9ced6;
  --white:#ffffff;
}
*{box-sizing:border-box;margin:0;padding:0}
html,body{width:1200px;height:4601px;overflow:hidden}
body{font-family:"Inter",Arial,sans-serif;color:var(--ink);background:var(--white);position:relative}
.abs{position:absolute}

/* top bar */
.topbar{position:absolute;left:0;top:0;width:1200px;height:43px;background:var(--blue);color:#fff;font-size:13px}
.topbar .mail{position:absolute;left:111px;top:13px;display:flex;gap:8px;align-items:center}
.topbar .call{position:absolute;right:110px;top:13px;display:flex;gap:8px;align-items:center}

/* nav */
.nav{position:absolute;left:0;top:43px;width:1200px;height:66px;background:#fff;box-shadow:0 2px 8px rgba(0,0,0,.08);z-index:3}
.brand{position:absolute;left:111px;top:10px;width:160px;text-align:center;color:var(--blue);font-weight:500;line-height:1}
.brand .b1{display:block;font-size:23px;letter-spacing:9px;font-weight:700}
.brand .b2{display:block;font-size:23px;letter-spacing:5px;margin-top:2px}
.menu{position:absolute;left:462px;top:27px;display:flex;gap:31px;font-size:13px;color:#2a2f38}
.menu .active{color:var(--yellow)}
.menu .active::before{content:"";position:absolute;top:-27px;width:42px;height:3px;background:var(--yellow)}
.nav .sep{position:absolute;left:1045px;top:18px;width:1px;height:30px;background:#ccd}
.nav .search{position:absolute;left:1073px;top:27px}

/* hero */
.hero{position:absolute;left:0;top:109px;width:1200px;height:555px;overflow:hidden}
.hero-photo{position:absolute;inset:0;background:linear-gradient(100deg,#f3f3f1 0%,#e9e8e4 45%,#d9d6cf 70%,#c9c4bb 100%)}
.hero-photo::after{content:"";position:absolute;left:640px;top:0;width:560px;height:555px;background:radial-gradient(ellipse at 60% 45%,rgba(240,120,40,.35),rgba(245,180,0,.15) 40%,rgba(0,0,0,0) 70%)}
.hero h1{position:absolute;left:111px;top:126px;font-size:52px;line-height:61px;color:var(--blue)}
.hero h1 b{display:block;font-weight:800}
.hero h1 span{display:block;font-weight:400;letter-spacing:1px}
.hero p{position:absolute;left:111px;top:255px;width:370px;font-size:14.5px;line-height:26px;color:#4a5260}
.btn{display:inline-flex;align-items:center;gap:6px;border-radius:22px;font-weight:700;font-size:13px;color:#fff;height:42px;padding:0 26px}
.hero .btn{position:absolute;left:111px;top:320px;background:var(--yellow)}
.circle-arrow{position:absolute;width:42px;height:42px;border-radius:50%;background:#fff;display:flex;align-items:center;justify-content:center;box-shadow:0 1px 4px rgba(0,0,0,.15)}

/* about */
.about{position:absolute;left:0;top:664px;width:1200px;height:652px}
.hex-photo{position:absolute;left:111px;top:70px;width:428px;height:512px;clip-path:polygon(50% 0,100% 25%,100% 75%,50% 100%,0 75%,0 25%);background:linear-gradient(160deg,#e6e2da 0%,#b5b7b8 40%,#3d4b63 75%,#2b2d33 100%)}
.hex-frame{position:absolute;left:111px;top:59px}
.about h2{position:absolute;left:600px;top:104px;font-size:44px;color:var(--blue);font-weight:400;white-space:nowrap}
.about h2 b{font-weight:800}
.about .copy{position:absolute;left:600px;top:172px;width:478px;font-size:14.5px;line-height:26px;color:var(--muted);text-align:justify}
.about .copy p+p{margin-top:26px}
.about .btn{position:absolute;left:600px;top:504px;background:var(--blue);padding:0 24px}

/* service bands */
.band{position:absolute;left:0;width:1200px;height:407px;overflow:hidden}
.band svg.bg{position:absolute;left:0;top:0}
.band .photo{position:absolute;top:14px;height:379px}
.band-a .photo{left:598px;width:475px;clip-path:polygon(26% 0,100% 0,100% 100%,0 100%)}
.band-b .photo{left:127px;width:477px;clip-path:polygon(0 0,74% 0,100% 100%,0 100%)}
.band .text{position:absolute;top:75px;width:418px;color:#fff}
.band-a .text{left:162px}
.band-b .text{left:629px}
.band h3{font-size:34px;line-height:42px;font-weight:400}
.band h3 b{font-weight:800}
.band p{margin-top:10px;font-size:14.5px;line-height:26px;text-align:justify}

/* testimonials */
.reviews{position:absolute;left:0;top:2943px;width:1200px;height:602px}
.reviews h2{position:absolute;left:0;width:1200px;top:96px;text-align:center;font-size:44px;font-weight:400;color:var(--blue)}
.reviews h2 b{font-weight:800}
.card{position:absolute;top:179px;width:465px;height:236px;background:#fff;border-top:4px solid var(--yellow);box-shadow:0 3px 14px rgba(0,0,0,.1);padding:38px 26px 0}
.card p{font-size:14px;line-height:26px;color:var(--muted)}
.card .rating{margin-top:20px;font-size:13px;color:var(--muted);display:flex;align-items:center;gap:16px}
.card .stars{color:var(--yellow);letter-spacing:6px;font-size:16px}
.card::after{content:"";position:absolute;left:60px;bottom:-38px;border-left:0 solid transparent;border-right:48px solid transparent;border-top:38px solid #fff;filter:drop-shadow(0 4px 3px rgba(0,0,0,.06))}
.person{position:absolute;top:453px;display:flex;gap:20px;align-items:center}
.avatar{width:64px;height:64px;border-radius:50%;background:linear-gradient(160deg,#d7dbe2,#7a8494)}
.person strong{display:block;font-size:18px;color:var(--ink);font-weight:600}
.person span{display:block;font-size:14px;color:var(--muted);margin-top:4px}
.reviews .circle-arrow{top:342px;border:1px solid #d2d6dd;box-shadow:none;width:38px;height:38px}

/* contact */
.contact-photo{position:absolute;left:0;top:3684px;width:1200px;height:491px;background:linear-gradient(100deg,#cdd2d8 0%,#9fa9b6 35%,#6c7a8c 55%,#d8c043 75%,#4f5b6b 100%)}
.contact-card{position:absolute;left:82px;top:3585px;width:522px;height:558px;background:#fff;box-shadow:0 4px 18px rgba(0,0,0,.12)}
.contact-card h2{position:absolute;left:29px;top:32px;font-size:44px;font-weight:400;color:var(--blue)}
.contact-card h2 b{font-weight:800}
.field{position:absolute;left:27px;width:470px;height:62px;border:1px solid var(--line);font-size:13.5px;color:#6a7280;padding:20px 27px}
.field.msg{height:170px}
.send{position:absolute;left:411px;top:459px;width:57px;height:57px;border-radius:50%;background:var(--yellow);display:flex;align-items:center;justify-content:center}

/* footer */
.footer{position:absolute;left:0;top:4175px;width:1200px;height:426px;background:linear-gradient(180deg,#1a4fa0 0%,#164693 60%,#123d86 100%);color:#fff}
.footer .brand-f{position:absolute;left:170px;top:112px;width:220px;text-align:center;font-weight:500;line-height:1}
.footer .brand-f .b1{display:block;font-size:34px;letter-spacing:14px;font-weight:700}
.footer .brand-f .b2{display:block;font-size:34px;letter-spacing:7px;margin-top:4px}
.socials{position:absolute;left:203px;top:227px;display:flex;gap:16px}
.socials i{display:block;width:26px;height:26px;border-radius:50%;border:2px solid rgba(255,255,255,.8)}
.socials i.on{background:var(--yellow);border-color:var(--yellow)}
.footer h4{position:absolute;top:100px;font-size:24px;font-weight:700}
.links{position:absolute;left:559px;top:158px;list-style:none;font-size:14px}
.links li{height:26px;display:flex;gap:22px}
.links li::before{content:"»";opacity:.85}
.cinfo{position:absolute;left:800px;top:152px;font-size:14px;line-height:24px}
.cinfo div{position:absolute;left:0;display:flex;gap:14px;white-space:nowrap}
.cinfo .ic{width:30px;height:30px;border-radius:50%;background:var(--yellow);flex:none;display:flex;align-items:center;justify-content:center}
.footer .rule{position:absolute;left:0;top:335px;width:1200px;height:1px;background:rgba(255,255,255,.25)}
.footer .copy{position:absolute;left:0;width:1200px;top:364px;text-align:center;font-size:16px}
</style>
</head>
<body>

<header class="topbar">
  <div class="mail">
    <svg width="13" height="10" viewBox="0 0 13 10"><rect x="0" y="0" width="13" height="10" rx="1" fill="#f5b400"/><path d="M0.5 1 L6.5 5.5 L12.5 1" stroke="#0d3f8e" stroke-width="1.2" fill="none"/></svg>
    Mail Us : info@companyname.com
  </div>
  <div class="call">
    <svg width="12" height="12" viewBox="0 0 24 24"><path fill="#f5b400" d="M6.6 10.8a15.1 15.1 0 0 0 6.6 6.6l2.2-2.2c.3-.3.7-.4 1-.2 1.1.4 2.3.6 3.6.6.6 0 1 .4 1 1V20c0 .6-.4 1-1 1C10.6 21 3 13.4 3 4c0-.6.4-1 1-1h3.5c.6 0 1 .4 1 1 0 1.3.2 2.5.6 3.6.1.3 0 .7-.2 1z"/></svg>
    Call Us Today : +1 888 888 8888
  </div>
</header>

<nav class="nav">
  <div class="brand"><span class="b1">QUILL</span><span class="b2">ELECTRIC</span></div>
  <div class="menu">
    <span class="active">HOME</span><span>ABOUT US</span><span>SERVICES</span><span>PROJECTS</span><span>COMMUNITY</span><span>CONTACT</span>
  </div>
  <div class="sep"></div>
  <svg class="search" width="13" height="13" viewBox="0 0 14 14"><circle cx="5.5" cy="5.5" r="4.3" stroke="#f5b400" stroke-width="2" fill="none"/><path d="M8.8 8.8 L13 13" stroke="#f5b400" stroke-width="2.2"/></svg>
</nav>

<section class="hero">
  <div class="hero-photo" role="img" aria-label="Electrician in hard hat and hi-vis jacket installing a ceiling fitting from a yellow ladder in a bright room"></div>
  <h1><b>QUILL</b><span>ELECTRIC</span></h1>
  <p>Lorem ipsum dolor sit amet, consectetur adipiscing elit, seddo eius mod dolore magna aliqua.</p>
  <span class="btn">GET STARTED
    <svg width="12" height="12" viewBox="0 0 12 12"><circle cx="6" cy="6" r="6" fill="#fff"/><path d="M5 3.5 L7.5 6 L5 8.5" stroke="#f5b400" stroke-width="1.6" fill="none"/></svg>
  </span>
  <div class="circle-arrow" style="left:111px;top:443px"><svg width="10" height="10" viewBox="0 0 10 10"><path d="M6.5 1.5 L3 5 L6.5 8.5" stroke="#222" stroke-width="1.6" fill="none"/></svg></div>
  <div class="circle-arrow" style="left:163px;top:443px"><svg width="10" height="10" viewBox="0 0 10 10"><path d="M3.5 1.5 L7 5 L3.5 8.5" stroke="#222" stroke-width="1.6" fill="none"/></svg></div>
</section>

<section class="about">
  <svg class="hex-frame" width="428" height="140" viewBox="0 0 428 140">
    <defs><linearGradient id="hexline" x1="0" x2="1" y1="0" y2="0"><stop offset="0" stop-color="#0d3f8e"/><stop offset="1" stop-color="#f5b400"/></linearGradient></defs>
    <path d="M78 94 L78 58 L214 0 L350 58 L350 110" stroke="url(#hexline)" stroke-width="16" fill="none"/>
  </svg>
  <div class="hex-photo" role="img" aria-label="Electrician wearing a yellow hard hat, ear defenders and tool apron, carrying a toolbox"></div>
  <h2><b>ABOUT</b> QUILL ELECTRIC</h2>
  <div class="copy">
    <p>Lorem ipsum dolor sit amet, consectetur adipiscing elit, sed do eiusm od tempor incididunt ut labore et dolore magna aliqua. Ut enim ad mi nim veniam, quis nostrud exercitation ullamco laboris nisi ut aliquip ex ea commodo consequat. Duis aute irure dolor in reprehenderit in volu ptate velit esse cillum dolore eu fugiat nulla pariatur. Excepteur sint occaecat cupidatat non proident, sunt in culpa qui officia deserunt mollit anim id est laborum.</p>
    <p>Lorem ipsum dolor sit amet, consectetur adipiscing elit, sed do eiusmod tempor incididunt ut labore et dolore magna aliqua. Ut enim ad minim veniam, quis nostrud exercitation ullamco laboris nisi ut aliquip ex ea commodo consequat.</p>
  </div>
  <span class="btn">LEARN MORE
    <svg width="12" height="12" viewBox="0 0 12 12"><circle cx="6" cy="6" r="6" fill="#fff"/><path d="M5 3.5 L7.5 6 L5 8.5" stroke="#0d3f8e" stroke-width="1.6" fill="none"/></svg>
  </span>
</section>

<section class="band band-a" style="top:1316px">
  <svg class="bg" width="1200" height="407"><rect width="1200" height="407" fill="#0d3f8e"/><polygon points="840,0 1200,0 1200,407 670,407" fill="#f5b400"/></svg>
  <div class="photo" role="img" aria-label="Hands testing wiring in an electrical distribution cabinet" style="background:linear-gradient(135deg,#c9c3b6,#6f6a63 50%,#2f3035)"></div>
  <div class="text">
    <h3><b>SITE ELECTRICAL</b><br>EXPERIENCE</h3>
    <p>Lorem ipsum dolor sit amet, consectetur adipiscing elit, sed do eiusm od tempor incididunt ut labore et dolore magna aliqua. Ut enim ad mi nim veniam, quis nostrud exercitation ullamco laboris nisi ut aliquip ex ea commodo consequat. Duis aute irure dolor in reprehenderit in volu ptate velit esse cillum dolore eu fugiat nulla pariatur.</p>
  </div>
</section>

<section class="band band-b" style="top:1723px">
  <svg class="bg" width="1200" height="407"><rect width="1200" height="407" fill="#0d3f8e"/><polygon points="0,0 357,0 520,407 0,407" fill="#f5b400"/></svg>
  <div class="photo" role="img" aria-label="Steel power transmission tower against a blue evening sky" style="background:linear-gradient(160deg,#4a5f8c,#7f8fb2 50%,#b99a8e)"></div>
  <div class="text">
    <h3><b>POWER DISTRIBUTION</b><br>EXPERIENCE</h3>
    <p>Lorem ipsum dolor sit amet, consectetur adipiscing elit, sed do eiusm od tempor incididunt ut labore et dolore magna aliqua. Ut enim ad mi nim veniam, quis nostrud exercitation ullamco laboris nisi ut aliquip ex ea commodo consequat. Duis aute irure dolor in reprehenderit in volu ptate velit esse cillum dolore eu fugiat nulla pariatur.</p>
  </div>
</section>

<section class="band band-a" style="top:2130px">
  <svg class="bg" width="1200" height="407"><rect width="1200" height="407" fill="#0d3f8e"/><polygon points="840,0 1200,0 1200,407 670,407" fill="#f5b400"/></svg>
  <div class="photo" role="img" aria-label="Couple on a step ladder fitting a pendant light in a bright white room" style="background:linear-gradient(135deg,#eef0f2,#d5d8dc 55%,#a9aeb6)"></div>
  <div class="text">
    <h3><b>LIGHTING</b> EXPERIENCE</h3>
    <p>Lorem ipsum dolor sit amet, consectetur adipiscing elit, sed do eiusm od tempor incididunt ut labore et dolore magna aliqua. Ut enim ad mi nim veniam, quis nostrud exercitation ullamco laboris nisi ut aliquip ex ea commodo consequat. Duis aute irure dolor in reprehenderit in volu ptate velit esse cillum dolore eu fugiat nulla pariatur. Lorem ipsum dolor sit amet, consectetur adipiscing elit, sed do eiusmod tempor incididunt ut labore et dolore magna aliqua.</p>
  </div>
</section>

<section class="band band-b" style="top:2537px">
  <svg class="bg" width="1200" height="407"><rect width="1200" height="407" fill="#0d3f8e"/><polygon points="0,0 357,0 520,407 0,407" fill="#f5b400"/></svg>
  <div class="photo" role="img" aria-label="Electrician in white hard hat and hi-vis vest checking an electrical panel with a clipboard" style="background:linear-gradient(135deg,#8e9aa6,#b9c0c7 40%,#b8c94a 75%,#3b3f45)"></div>
  <div class="text">
    <h3><b>PANEL</b> EXPERIENCE</h3>
    <p>Lorem ipsum dolor sit amet, consectetur adipiscing elit, sed do eiusm od tempor incididunt ut labore et dolore magna aliqua. Ut enim ad mi nim veniam, quis nostrud exercitation ullamco laboris nisi ut aliquip ex ea commodo consequat. Duis aute irure dolor in reprehenderit in volu ptate velit esse cillum dolore eu fugiat nulla pariatur. Lorem ipsum dolor sit amet, consectetur adipiscing elit, sed do eiusmod tempor incididunt ut labore et dolore magna aliqua.</p>
  </div>
</section>

<section class="reviews">
  <h2><b>WHAT</b> PEOPLE SAYS</h2>
  <div class="circle-arrow" style="left:36px"><svg width="9" height="9" viewBox="0 0 10 10"><path d="M6.5 1.5 L3 5 L6.5 8.5" stroke="#444" stroke-width="1.4" fill="none"/></svg></div>
  <div class="circle-arrow" style="left:1126px"><svg width="9" height="9" viewBox="0 0 10 10"><path d="M3.5 1.5 L7 5 L3.5 8.5" stroke="#444" stroke-width="1.4" fill="none"/></svg></div>

  <div class="card" style="left:111px">
    <p>Lorem ipsum dolor sit amet, consectetur adipiscing elit, sed do eiusm od tempor incididunt ut labore et dolore magna aliqua. Ut enim ad mi nim veniam, quis nostrud exercitation ullamco laboris nisi ut aliquip ex ea commodo consequat. Duis aute irure dolor in reprehenderit</p>
    <div class="rating"><span class="stars">★★★★★</span>4.5 reviews</div>
  </div>
  <div class="person" style="left:182px">
    <div class="avatar" role="img" aria-label="Customer portrait"></div>
    <div><strong>Dara Wilkes</strong><span>Company name</span></div>
  </div>

  <div class="card" style="left:623px">
    <p>Lorem ipsum dolor sit amet, consectetur adipiscing elit, sed do eiusm od tempor incididunt ut labore et dolore magna aliqua. Ut enim ad mi nim veniam, quis nostrud exercitation ullamco laboris nisi ut aliquip ex ea commodo consequat. Duis aute irure dolor in reprehenderit</p>
    <div class="rating"><span class="stars">★★★★★</span>4.5 reviews</div>
  </div>
  <div class="person" style="left:694px">
    <div class="avatar" role="img" aria-label="Customer portrait"></div>
    <div><strong>Dara Wilkes</strong><span>Company name</span></div>
  </div>
</section>

<div class="contact-photo" role="img" aria-label="Smiling electrician in blue hard hat and yellow hi-vis vest working on a ceiling air unit"></div>
<section class="contact-card">
  <h2><b>GET</b> IN TOUCH</h2>
  <div class="field" style="top:98px">Name</div>
  <div class="field" style="top:171px">Email address</div>
  <div class="field" style="top:244px">Phone</div>
  <div class="field msg" style="top:317px">Message</div>
  <div class="send"><svg width="22" height="22" viewBox="0 0 24 24"><path fill="#fff" d="M22 2 L2 10.5 L9 13 L11.5 20 Z"/><path d="M22 2 L9 13" stroke="#f5b400" stroke-width="1.4"/></svg></div>
</section>

<footer class="footer">
  <div class="brand-f"><span class="b1">QUILL</span><span class="b2">ELECTRIC</span></div>
  <div class="socials"><i></i><i class="on"></i><i></i><i></i></div>

  <h4 style="left:559px">Quick Links</h4>
  <ul class="links">
    <li>Home</li><li>About</li><li>Services</li><li>Projects</li><li>Community</li><li>Contact us</li>
  </ul>

  <h4 style="left:798px">Contact us</h4>
  <div class="cinfo">
    <div style="top:0"><span class="ic"><svg width="12" height="14" viewBox="0 0 12 14"><path fill="#fff" d="M6 0a5 5 0 0 0-5 5c0 3.6 5 9 5 9s5-5.4 5-9a5 5 0 0 0-5-5zm0 7a2 2 0 1 1 0-4 2 2 0 0 1 0 4z"/></svg></span><span>123, Lorem ipsum dolor<br>California</span></div>
    <div style="top:78px"><span class="ic"><svg width="13" height="13" viewBox="0 0 24 24"><path fill="#fff" d="M6.6 10.8a15.1 15.1 0 0 0 6.6 6.6l2.2-2.2c.3-.3.7-.4 1-.2 1.1.4 2.3.6 3.6.6.6 0 1 .4 1 1V20c0 .6-.4 1-1 1C10.6 21 3 13.4 3 4c0-.6.4-1 1-1h3.5c.6 0 1 .4 1 1 0 1.3.2 2.5.6 3.6.1.3 0 .7-.2 1z"/></svg></span><span style="line-height:30px">+1 888 888 8888</span></div>
    <div style="top:130px"><span class="ic"><svg width="13" height="10" viewBox="0 0 13 10"><rect width="13" height="10" rx="1" fill="#fff"/><path d="M0.5 1 L6.5 5.5 L12.5 1" stroke="#f5b400" stroke-width="1.2" fill="none"/></svg></span><span style="line-height:30px">info@companyname.com</span></div>
  </div>

  <div class="rule"></div>
  <div class="copy">© Copyrights 2024 | All Rights Reserved</div>
</footer>

</body>
</html>
```